Real Estate Company Needs Business Card Designed

We need a business card design for a new real estate company based in Campbell, CA (Silicon Valley). We plan to improve the residential real estate industry by using technology to improve customer experience. We would like to see designs that use a black background. The final design should communicate sophistication and customer service, as well as stability and technology.

Industry/Entity Type

Real Estate

Requirements
Must have
• Black background

```html
<!DOCTYPE html>
<html lang="en">
<head>
<meta charset="UTF-8">
<title>Veloria Business Card</title>
<link href="https://fonts.googleapis.com/css2?family=Montserrat:wght@500&family=Ubuntu:wght@700&family=Crimson+Pro:ital,wght@1,600&display=swap" rel="stylesheet">
<style>
  :root {
    --card-black: #050505;
    --band-deep: #0b0f17;
    --band-mid: #1d2634;
    --band-light: #2c3646;
    --brand-blue: #b9c9e6;
    --name-ice: #cfe4f1;
    --text-white: #ffffff;
    --rule-steel: #5a6b86;
  }
  html, body {
    margin: 0;
    padding: 0;
    width: 1200px;
    height: 686px;
    overflow: hidden;
    background: var(--card-black);
  }
  .card {
    position: relative;
    width: 1200px;
    height: 686px;
    background: var(--card-black);
    overflow: hidden;
  }
  .texture-band {
    position: absolute;
    left: 0;
    top: 0;
    width: 1175px;
    height: 297px;
    background: linear-gradient(100deg, var(--band-deep) 0%, var(--band-mid) 35%, var(--band-light) 65%, var(--band-mid) 100%);
  }
  .guide-vertical {
    position: absolute;
    left: 283px;
    top: 0;
    width: 1px;
    height: 503px;
    background: var(--rule-steel);
  }
  .guide-horizontal {
    position: absolute;
    left: 283px;
    top: 503px;
    width: 917px;
    height: 1px;
    background: var(--rule-steel);
  }
  .brand-name {
    position: absolute;
    left: 326px;
    top: 28px;
    width: 834px;
    margin: 0;
    font-family: "Montserrat", sans-serif;
    font-weight: 500;
    font-size: 142px;
    line-height: 1;
    letter-spacing: 6px;
    color: var(--brand-blue);
    text-align: center;
  }
  .agent-name {
    position: absolute;
    left: 420px;
    top: 292px;
    width: 400px;
    margin: 0;
    font-family: "Ubuntu", sans-serif;
    font-weight: 700;
    font-size: 35px;
    line-height: 1.2;
    color: var(--name-ice);
    text-align: center;
  }
  .agent-title {
    position: absolute;
    left: 420px;
    top: 342px;
    width: 400px;
    margin: 0;
    font-family: "Crimson Pro", serif;
    font-style: italic;
    font-weight: 600;
    font-size: 35px;
    line-height: 1.2;
    color: var(--text-white);
    text-align: center;
  }
  .contact {
    position: absolute;
    left: 282px;
    top: 472px;
    margin: 0;
    font-family: "Crimson Pro", serif;
    font-style: italic;
    font-weight: 600;
    font-size: 36px;
    line-height: 38px;
    color: var(--text-white);
  }
  .contact span { display: block; }
</style>
</head>
<body>
  <div class="card">
    <div class="texture-band" role="img" aria-label="Dark blue-grey field of small repeating triangular shapes"></div>
    <div class="guide-vertical"></div>
    <div class="guide-horizontal"></div>
    <h1 class="brand-name">VELORIA</h1>
    <p class="agent-name">Marisol T Aranda</p>
    <p class="agent-title">Real Estate Agent</p>
    <p class="contact">
      <span class="contact-email">marisolaranda@lumenmail.com</span>
      <span class="contact-phone">408.555.0172</span>
    </p>
  </div>
</body>
</html>
```